Redesign of Plastic Surgeon Website to fully responsive / modern feel

Hi

Our current website is out of date www.harbourlinecosmetic.org

We want a fresh / modern looking design
Needs to be fully responsive design that works extremely well on ipad and mobile device

Would like design for both full screen website and mobile

Have listed a few websites of other plastic surgeons we like
http://www.reformclinicdaily.com/
http://www.peterholtbymd.com/
http://www.corvanbeauty.com/
http://www.tidewellcontouring.com/

Menu needs to include
1. About Us
2. Procedures (see current website for example)
3. News
4. Patient Resources
5. Contact Us

We are flexible with colours / images / layout

I have uploaded a document that has some content - the face pages content is completed only

some of the procedures can have content upwards of 4000 words - total website can be large with over 40,000 words
Updates

Target Market(s)

Mainly women 20-60 85% of practice
Some men 15%

Industry/Entity Type

Plastic Surgery

Number of Pages Required

5+ page

Requirements
Must have
• We need designs for
• Homepage
• Internal pages
• 1. Landing pages for breast / body / face / non surgical main pages
• 2. Procedure pages for individual pages under each section - eg breast augmentation
• 3. About us pages - like meet the doctor, our staff, clinics
• 4. Contact page
• 5. Blog / News page
Nice to have
• See our list of websites for examples of designs we like
• Like full screen design with nice hero image
• Needs to have good to call to action messages on home page like
• Specials, procedure of the month, etc

```html
<!DOCTYPE html>
<html lang="en">
<head>
<meta charset="utf-8">
<title>Harbourline Cosmetic Institute</title>
<link href="https://fonts.googleapis.com/css2?family=Open+Sans:wght@400;600;700&display=swap" rel="stylesheet">
<style>
:root{
  --ink:#3a414b;
  --body:#4a4f57;
  --muted:#8a8f96;
  --link:#5a6f98;
  --sky:#9bd3f0;
  --sand:#f5f2ee;
  --hero-a:#9aa9c2;
  --hero-b:#6f82a6;
  --white:#ffffff;
}
*{margin:0;padding:0;box-sizing:border-box}
html,body{width:1200px;height:2314px;overflow:hidden;background:var(--white)}
body{font-family:"Open Sans",sans-serif;color:var(--body);position:relative}
.abs{position:absolute}

.topbar{left:0;top:0;width:1200px;height:28px;background:var(--white)}
.nav{left:440px;top:9px;display:flex;gap:14px;font-size:8px;font-weight:700;color:var(--ink);letter-spacing:.2px}
.phone{left:954px;top:6px;font-size:12px;font-weight:600;color:var(--ink)}

.hero{left:0;top:28px;width:1200px;height:353px;background:linear-gradient(90deg,var(--hero-a) 0%,#8798b6 45%,var(--hero-b) 100%)}
.hero-photo{left:600px;top:0;width:480px;height:353px;background:radial-gradient(ellipse at 55% 45%,#c9b2a6 0%,#8e8592 45%,rgba(111,130,166,0) 75%)}
.hero-title{left:231px;top:72px;width:362px;color:var(--white);font-size:16.5px;font-weight:600;text-align:center;line-height:1.4}
.hero-text{left:231px;top:146px;width:345px;color:var(--white);font-size:11px;font-weight:600;line-height:1.45}
.dots{left:570px;top:322px;display:flex;gap:8px}
.dots span{width:8px;height:8px;border-radius:50%;background:#a9d0ef}
.dots span.on{background:var(--white);width:10px;height:10px;margin-top:-1px}

.h2{width:1200px;text-align:center;color:var(--ink);font-weight:600}
.proc-title{top:408px;font-size:20px}
.proc-col{width:200px;text-align:center}
.proc-icon{width:78px;height:78px;margin:0 auto;border-radius:3px}
.proc-name{margin-top:17px;font-size:12px;font-weight:700;color:var(--ink)}
.proc-links{margin-top:14px;font-size:11.5px;line-height:16px;color:var(--link)}

.meet{left:0;top:712px;width:1200px;height:278px;background:linear-gradient(90deg,var(--sand),#f7f5f2 60%,#fbfbfa);box-shadow:0 3px 4px rgba(0,0,0,.18)}
.meet-title{left:234px;top:762px;font-size:29px;font-weight:600;color:var(--ink)}
.meet-text{left:232px;top:834px;width:490px;font-size:12px;line-height:22px}
.doctor{left:771px;top:726px;width:250px;height:264px;background:linear-gradient(180deg,#e6d8cc 0%,#c9b7a8 35%,#4a4d55 70%,#3c3f46 100%);border-radius:100px 100px 0 0}

.cool-title{top:1030px;font-size:20px}
.gallery{left:278px;top:1100px;width:643px;height:226px;box-shadow:3px 3px 5px rgba(0,0,0,.3);display:grid;grid-template-columns:160px 161px 161px 161px;grid-template-rows:113px 113px}
.gallery div{border:1px solid #fff}
.g1{background:linear-gradient(135deg,#d9c3b4,#b8aab0)}
.g2{background:linear-gradient(135deg,#efe0d4,#c9a58a)}
.g3{background:linear-gradient(135deg,#c7d0dc,#8a9db5)}
.g4{background:linear-gradient(135deg,#dcd8d6,#b7b0ad)}
.g5{background:linear-gradient(135deg,#f0f0f0,#c8ccd2)}
.g6{grid-column:span 2;background:linear-gradient(135deg,#cfc0b4,#7d8088)}
.g7{background:linear-gradient(135deg,#e6e9ee,#a9b2bd)}
.cool-text{left:353px;top:1362px;width:494px;text-align:center;font-size:12px;line-height:22px}

.month{left:0;top:1522px;width:1200px;height:241px;background:var(--sky)}
.month-title{left:237px;top:1563px;font-size:20px;font-weight:600;color:var(--ink)}
.month-text{left:234px;top:1606px;width:420px;font-size:12px;line-height:22px;color:var(--ink)}
.btn{left:234px;top:1691px;width:84px;height:23px;background:var(--white);font-size:11px;color:var(--ink);text-align:center;line-height:23px;font-weight:600}
.month-photo{left:715px;top:1522px;width:250px;height:241px;background:linear-gradient(160deg,#e8d8cf 0%,#cdb7ab 45%,#f1efef 100%);box-shadow:4px 4px 8px rgba(0,0,0,.35)}

.contact-title{top:1810px;font-size:30px}
.contact-box{left:234px;top:1898px;width:731px;height:333px;background:var(--sand)}
.field{left:341px;width:206px;height:31px;background:var(--white);font-size:11px;font-weight:700;color:var(--sky);padding:8px 18px}
.send{left:341px;top:2163px;width:84px;height:25px;background:var(--sky);color:var(--white);font-size:11px;font-weight:700;text-align:center;line-height:25px}
.clinic h3{font-size:16px;font-weight:700;color:var(--ink);margin-bottom:6px}
.clinic p{font-size:12px;line-height:22px;color:var(--muted)}
</style>
</head>
<body>
<header class="abs topbar">
  <nav class="abs nav"><span>HOME</span><span>ABOUT US</span><span>PROCEDURES</span><span>NEWS</span><span>PATIENT RESOURCES</span><span>CONTACT US</span></nav>
  <div class="abs phone">+61 (02) 9000 4812</div>
</header>

<section class="abs hero">
  <div class="abs hero-photo" role="img" aria-label="Portrait photograph of a smiling woman with long dark hair"></div>
</section>
<h1 class="abs hero-title">At the Harbourline Cosmetic Institute - Your future looks beautiful</h1>
<p class="abs hero-text">You can expect beautiful results at the Harbourline Cosmetic Institute. Offering<br>unparalleled expertise in face, breast and body enhancement, including facelifts, breast<br>augmentation / lift / reduction or tummy tucks, we offer total care at every step of your transformative journey.</p>
<div class="abs dots"><span></span><span class="on"></span><span></span><span></span></div>

<h2 class="abs h2 proc-title">PROCEDURES</h2>
<div class="abs proc-col" style="left:219px;top:460px">
  <div class="proc-icon" role="img" aria-label="Photo of a toned midriff" style="background:linear-gradient(180deg,#d8c2b2,#3a3234 70%,#d6c0b0)"></div>
  <div class="proc-name">BODY</div>
  <div class="proc-links">Tummy Tuck<br>Labiaplasty<br>Liposuction<br>Brazilian Butt Lift<br>Mummy Makeover</div>
</div>
<div class="abs proc-col" style="left:407px;top:460px">
  <div class="proc-icon" role="img" aria-label="Photo of facial surgery markings" style="background:linear-gradient(135deg,#cfdbe8,#e9d9cc)"></div>
  <div class="proc-name">FACE</div>
  <div class="proc-links">Facelift | Browlift<br>Rhinoplasty<br>Blepharoplasty<br>Otoplasty</div>
</div>
<div class="abs proc-col" style="left:592px;top:460px">
  <div class="proc-icon" role="img" aria-label="Photo of a cosmetic injection treatment" style="background:linear-gradient(135deg,#f1e3e0,#dcc3bd)"></div>
  <div class="proc-name">NON SURGICAL</div>
  <div class="proc-links">Anti Wrinkle<br>Dermal Fillers<br>CryoContour<br>SonoForm</div>
</div>
<div class="abs proc-col" style="left:782px;top:460px">
  <div class="proc-icon" role="img" aria-label="Photo of a torso for breast procedures" style="background:linear-gradient(135deg,#f0c9ad,#d99b7c)"></div>
  <div class="proc-name">BREAST</div>
  <div class="proc-links">Breast Augmentation<br>Breast Lift<br>Breast Lift with Implants<br>Breast Reduction<br>Gynaecomastia<br>Mummy Makeover</div>
</div>

<section class="abs meet"></section>
<h2 class="abs meet-title">Meet Dr Hale</h2>
<p class="abs meet-text">Dr Hale is one of Australia’s most eminent specialists in plastic and cosmetic surgery, and is supported by our highly qualified, professional team. As Sydney’s premier plastic surgery clinic, we use only the most revolutionary techniques to minimise scarring to help you look better, feel better and enjoy a beautiful new you.</p>
<div class="abs doctor" role="img" aria-label="Portrait photograph of the surgeon in a suit and glasses"></div>

<h2 class="abs h2 cool-title">CryoContour / SonoForm</h2>
<div class="abs gallery" role="img" aria-label="Collage of body contouring treatments and equipment">
  <div class="g1"></div><div class="g2"></div><div class="g3"></div><div class="g4"></div>
  <div class="g5"></div><div class="g6"></div><div class="g7"></div>
</div>
<p class="abs cool-text">CryoContour and SonoForm are both FDA-approved and the treatments require no downtime or recovery time. Because of this, they are ideal for anyone who is not able to spend a few days recovering from a procedure. With both treatments, it can take a few weeks to see the full results so if you are preparing for an event, you’ll want to schedule your treatments a few weeks in advanced.</p>

<section class="abs month"></section>
<h2 class="abs month-title">Procedure of the month</h2>
<p class="abs month-text">Lorem ipsum dolor sit amet, no duo doming audire. Ut congue posidonium mel, nominavi incorrupte mei et. Ea vim principes conceptam delicatissimi, eu idque nullam graecis eum Mei idque dolores te</p>
<div class="abs btn">DETAILS</div>
<div class="abs month-photo" role="img" aria-label="Photo of a woman's face examined by gloved hands"></div>

<h2 class="abs h2 contact-title">CONTACT US</h2>
<section class="abs contact-box"></section>
<div class="abs field" style="top:1935px">FULL NAME</div>
<div class="abs field" style="top:1981px">EMAIL</div>
<div class="abs field" style="top:2029px;height:114px">MESSAGE</div>
<div class="abs send">SEND</div>

<div class="abs clinic" style="left:652px;top:1936px"><h3>Chatswood</h3><p>Fernlea Clinic<br>Suite 501<br>14 Linden Street<br>Chatswood 2067</p></div>
<div class="abs clinic" style="left:796px;top:1936px"><h3>Mona Vale</h3><p>Suite 202<br>Bayview Plaza<br>36 Marlow Street<br>Mona Vale 2103</p></div>
<div class="abs clinic" style="left:652px;top:2071px"><h3>Randwick</h3><p>Suite 26<br>Eastgate Private<br>Ashby Street<br>Randwick 2031</p></div>
<div class="abs clinic" style="left:796px;top:2068px"><h3>Erina</h3><p>Coastway Centre<br>Medical Centre<br>Corella Drive<br>Erina 2250</p></div>
</body>
</html>
```